A clean modern user interface design for a smart home control system

Design Brief: Smart Home Interface Development
Project Overview
We are initiating a new project to develop a sophisticated smart home interface. This interface will be the central hub for controlling and managing various aspects of a smart home, including CCTV, Smart TV, Quorvel TV, home cinema using Vantromere, lighting, shades, HVAC, and audio systems. With no pre-existing designs or frameworks, this project offers a unique opportunity to create a fresh and innovative interface from the ground up. We aim to take inspiration from Quorvel’s renowned UI/UX design style, which is celebrated for its elegance, simplicity, and intuitive user experience. Additionally, the design should include the ability to switch between ‘light’ and ‘dark’ modes, reflecting modern user preferences for customizable visual themes.
Objectives
•	Innovation: Create a cutting-edge interface that sets a new standard for smart home control systems, drawing inspiration from Quorvel’s clean, minimalistic, and user-friendly approach.
•	User-Centric Design: Develop an intuitive interface that caters to a broad range of users, ensuring that both tech-savvy individuals and those less familiar with smart technology can navigate it with ease.
•	Consistency: Establish a cohesive design language across the interface, maintaining uniformity in style, typography, and colour palette, while reflecting the sophistication and simplicity of Quorvel’s design ethos.
•	Light and Dark Modes: Design the interface with the capability to switch between light and dark modes, allowing users to choose their preferred visual style for different environments and personal preferences.
•	Responsiveness: Create a fully responsive interface in both Landsthat functions seamlessly across various screen sizes and devices, including tablets, smartphones, and in-wall panels.
•	Integration: Seamlessly incorporate controls for CCTV, Smart TV, Quorvel TV, lighting, shades, HVAC, and audio into a single, unified interface that allows users to manage all aspects of their smart home effortlessly.
Target Audience
The primary users of this interface are homeowners who desire a luxurious and intuitive smart home experience. The design should appeal to both advanced users who require comprehensive functionality and those who prioritize simplicity and elegance. Additionally, the interface should be straightforward for integrators who configure and maintain these systems.
Design Elements
1.	Overall Aesthetic
•	Style: Emulate Quorvel’s clean, minimalist, and modern aesthetic that conveys high-end luxury and sophistication.
•	Typography: Select modern, legible fonts that enhance readability, reflecting Quorvel’s preference for clear and elegant typefaces. Sans-serif fonts, similar to Quorvel’s system fonts like San Francisco, are recommended.
•	Colour Palette: Design a neutral colour palette with subtle, refined accents. Include both light and dark mode options, allowing users to choose between a brighter, more energetic theme and a darker, more subdued theme that is easier on the eyes in low-light environments.
•	Icons: Design custom, vector-based icons that are sleek, intuitive, and consistent, taking inspiration from Quorvel’s iconic design language.
2.	User Interface Components
•	Navigation: Implement a simplified, intuitive navigation system that allows users to easily access different control sections (e.g., lighting, audio, CCTV), similar to the seamless navigation found in Quorvel’s uXa and teluX interfaces.
•	Dashboard: Create a home dashboard that provides a clear overview of key system statuses and quick access to frequently used controls, with a design inspired by the clarity and organisation of Quorvel’s Pivot Deck. Ensure that the dashboard looks equally effective in both light and dark modes.
•	Control Pages:
•	CCTV: Design live camera feed pages with options for full-screen viewing, recording controls, and playback functionality, focusing on a clean and user-friendly layout that adapts well to both light and dark modes.
•	Smart TV/Quorvel TV: Develop control panels for power, volume, channel/menu navigation, and input switching, reflecting Quorvel’s approach to simplicity and ease of use, with clear visibility in both visual modes.
•	Lighting & Shades: Incorporate intuitive sliders or toggles for controlling individual or grouped lights and shades, with options for scene creation and activation, designed for seamless use in light and dark modes.
•	HVAC: Design user-friendly temperature controls, including settings for scheduling, mode selection, and real-time adjustments, inspired by Quorvel’s seamless integration of function and form. Ensure readability and ease of use in both visual themes.
•	Audio: Develop multi-room audio controls that allow users to select sources, adjust volume, and manage audio zones easily, taking cues from Quorvel’s focus on intuitive and enjoyable user experiences, with consistent performance across both light and dark modes.
3.	User Experience
•	Flow: Ensure a logical user journey with smooth transitions between different controls, mimicking Quorvel’s emphasis on seamless and intuitive navigation.
•	Feedback: Provide immediate and clear feedback for user actions, such as toggling a light or changing a temperature setting, inspired by the responsive and satisfying interactions found in Quorvel’s designs.
•	Accessibility: Incorporate accessibility features, such as adjustable text sizes and potential voice control integration, in line with Quorvel’s commitment to inclusivity and user accessibility.
4.	Technical Requirements
•	Photoshop Design: All designs should be created in Adobe Photoshop (.psd) with organized groups and layers. Interface elements must be grouped logically, allowing for quick export and bulk saving. Ensure that each component (buttons, icons, sliders, etc.) is easily identifiable and can be individually exported for development purposes. Include separate groups for light and dark mode elements to ensure consistency across themes.
•	Responsive Design: Ensure the designs are adaptable for different screen sizes and orientations, including tablets, smartphones, and in-wall panels.
•	Performance: Design elements should be optimized for quick loading and smooth operation, even when managing multiple devices simultaneously.
Success Criteria
•	A user interface that is well-received for its modern design, ease of use, and clear inspiration from Quorvel’s iconic design style.
•	A fully responsive design that performs seamlessly across all intended devices.
•	Positive feedback from users and integrators, with strong engagement metrics, particularly in how well the light and dark modes are received.
Additional Notes
We look forward to seeing a design that not only meets our objectives but also reflects the elegance, usability, and flexibility that Quorvel’s design style is renowned for, offering a seamless experience in both light and dark modes.

High end residential end user

```html
<!DOCTYPE html>
<html lang="en">
<head>
<meta charset="utf-8">
<title>Smart Home Control – Dark Mode</title>
<link rel="stylesheet" href="https://fonts.googleapis.com/css2?family=Exo+2:ital,wght@0,700;1,800;1,900&display=swap">
<style>
  :root {
    --bg-top: #010208;
    --bg-bottom: #0c2478;
    --blue: #2f55b2;
    --orange: #a83c16;
    --green: #13aa4c;
    --divider: #2f55b2;
    --text: #ffffff;
    --heat: #e5222a;
  }
  * { margin: 0; padding: 0; box-sizing: border-box; }
  html, body { width: 1200px; height: 616px; overflow: hidden; }
  body {
    position: relative;
    background: linear-gradient(180deg, var(--bg-top) 0%, #061346 35%, var(--bg-bottom) 100%);
    font-family: "Exo 2", sans-serif;
    color: var(--text);
  }
  .abs { position: absolute; }

  /* source tiles */
  .source-tile {
    position: absolute; top: 32px; width: 103px; height: 103px; border-radius: 20px;
    background: linear-gradient(135deg, var(--blue), var(--green));
    display: flex; align-items: center; justify-content: center;
  }
  .source-tile.quorvel { left: 84px; font-weight: 800; font-size: 17px; text-align: center; line-height: 1.1; }
  .source-tile.smart-tv { left: 201px; }
  .home-icon { left: 348px; top: 32px; }

  /* theme switch */
  .theme-label { left: 948px; top: 48px; width: 110px; text-align: center; font-size: 9px; font-style: italic; font-weight: 800; }
  .theme-toggle { left: 948px; top: 63px; }

  /* buttons */
  .btn {
    position: absolute; width: 175px; height: 50px;
    display: flex; align-items: center; justify-content: center;
    font-style: italic; font-weight: 900; font-size: 29px; letter-spacing: -0.5px;
    text-transform: uppercase;
  }
  .btn.warm { background: linear-gradient(90deg, var(--blue), var(--orange)); }
  .btn.cool { background: linear-gradient(90deg, var(--blue), var(--green)); }
  .btn.tv { left: 110px; }
  .btn.mode { left: 927px; }
  .btn.audio { left: 915px; }
  .btn.audio-on { text-transform: none; }

  .divider { position: absolute; top: 180px; width: 2px; height: 179px; background: var(--divider); }

  .section-title { font-style: italic; font-weight: 900; font-size: 30px; letter-spacing: -0.3px; }
  .temp-title { left: 549px; top: 168px; }
  .limit { left: 710px; font-style: italic; font-weight: 900; font-size: 31px; }
  .temp-reading { left: 581px; top: 264px; width: 90px; text-align: center; font-style: italic; font-weight: 900; font-size: 27px; }

  .camera-title { left: 112px; top: 420px; }
  .camera-rule { left: 71px; top: 458px; width: 787px; height: 2px; background: var(--divider); }
  .stream {
    position: absolute; top: 468px; width: 94px; height: 84px;
    background: linear-gradient(90deg, var(--blue), var(--orange));
  }
  .stream .num { position: absolute; left: 6px; top: 3px; font-style: italic; font-weight: 900; font-size: 11px; }
  .stream svg { position: absolute; left: 40px; top: 33px; }
  .speaker { left: 1110px; }
</style>
</head>
<body>

<div class="source-tile quorvel">Quorvel TV</div>
<div class="source-tile smart-tv">
  <svg width="80" height="56" viewBox="0 0 80 56" aria-label="Smart TV">
    <rect x="6" y="3" width="68" height="42" fill="none" stroke="#fff" stroke-width="3"/>
    <text x="40" y="30" fill="#fff" font-family="Exo 2, sans-serif" font-weight="700" font-size="12" text-anchor="middle">SMART TV</text>
    <rect x="36" y="45" width="8" height="5" fill="#fff"/>
    <rect x="26" y="50" width="28" height="3" rx="1.5" fill="#fff"/>
  </svg>
</div>

<svg class="abs home-icon" width="117" height="102" viewBox="0 0 117 102" aria-label="Home">
  <defs><linearGradient id="homeGrad" x1="0" x2="1"><stop offset="0" stop-color="#2f55b2"/><stop offset="1" stop-color="#13aa4c"/></linearGradient></defs>
  <path d="M58.5 0 L117 50 L95 50 L95 102 L66 102 L66 78 L51 78 L51 102 L22 102 L22 50 L0 50 Z" fill="url(#homeGrad)"/>
</svg>

<div class="abs theme-label">Theme: Dark Mode</div>
<svg class="abs theme-toggle" width="110" height="50" viewBox="0 0 110 50" aria-label="Theme switch">
  <rect x="0" y="0" width="110" height="50" rx="25" fill="#fff"/>
  <circle cx="25" cy="25" r="8" fill="#0a1a5a"/>
  <g stroke="#0a1a5a" stroke-width="1.6">
    <line x1="25" y1="10" x2="25" y2="14"/><line x1="25" y1="36" x2="25" y2="40"/>
    <line x1="10" y1="25" x2="14" y2="25"/><line x1="36" y1="25" x2="40" y2="25"/>
    <line x1="14" y1="14" x2="17" y2="17"/><line x1="33" y1="33" x2="36" y2="36"/>
    <line x1="14" y1="36" x2="17" y2="33"/><line x1="33" y1="17" x2="36" y2="14"/>
  </g>
  <circle cx="84" cy="25" r="22" fill="#0a1a5a"/>
  <path d="M80 10 A15 15 0 1 1 80 40 A11 15 0 1 0 80 10 Z" fill="#fff"/>
</svg>

<!-- TV controls -->
<svg class="abs" style="left:40px;top:204px" width="46" height="24" viewBox="0 0 46 24" aria-label="Volume icon">
  <defs><linearGradient id="iconGrad" x1="0" x2="1"><stop offset="0" stop-color="#2f55b2"/><stop offset="1" stop-color="#13aa4c"/></linearGradient></defs>
  <rect x="0" y="13" width="9" height="11" fill="url(#iconGrad)"/><rect x="12" y="9" width="9" height="15" fill="url(#iconGrad)"/>
  <rect x="24" y="4" width="9" height="20" fill="url(#iconGrad)"/><rect x="37" y="0" width="9" height="24" fill="url(#iconGrad)"/>
</svg>
<svg class="abs" style="left:40px;top:255px" width="46" height="29" viewBox="0 0 46 29" aria-label="Channel icon">
  <g fill="url(#iconGrad)">
    <rect x="0" y="0" width="13" height="12"/><rect x="16" y="0" width="13" height="12"/><rect x="33" y="0" width="13" height="12"/>
    <rect x="0" y="17" width="13" height="12"/><rect x="16" y="17" width="13" height="12"/><rect x="33" y="17" width="13" height="12"/>
  </g>
</svg>
<svg class="abs" style="left:45px;top:313px" width="41" height="38" viewBox="0 0 41 38" aria-label="Menu icon">
  <rect width="41" height="38" fill="url(#iconGrad)"/>
  <g stroke="#0a1a5a" stroke-width="1.4"><line x1="5" y1="8" x2="36" y2="8"/><line x1="5" y1="15" x2="36" y2="15"/><line x1="5" y1="22" x2="36" y2="22"/><line x1="5" y1="29" x2="36" y2="29"/></g>
</svg>

<div class="btn warm tv" style="top:180px">Volume</div>
<div class="btn warm tv" style="top:242px">Channel</div>
<div class="btn warm tv" style="top:309px">Menu</div>

<div class="divider" style="left:304px"></div>

<svg class="abs" style="left:342px;top:196px" width="148" height="148" viewBox="0 0 148 148" aria-label="Direction pad">
  <defs><linearGradient id="padGrad" x1="0" x2="1"><stop offset="0" stop-color="#2f55b2"/><stop offset="1" stop-color="#13aa4c"/></linearGradient>
  <clipPath id="padClip"><circle cx="74" cy="74" r="74"/></clipPath></defs>
  <g clip-path="url(#padClip)">
    <circle cx="74" cy="74" r="74" fill="url(#padGrad)"/>
    <g stroke="#07144a" stroke-width="12"><line x1="0" y1="0" x2="148" y2="148"/><line x1="148" y1="0" x2="0" y2="148"/></g>
  </g>
  <g fill="#fff">
    <path d="M74 13 L84 30 L64 30 Z"/><path d="M74 135 L84 118 L64 118 Z"/>
    <path d="M12 74 L29 64 L29 84 Z"/><path d="M136 74 L119 64 L119 84 Z"/>
  </g>
</svg>

<div class="divider" style="left:513px"></div>

<!-- HVAC -->
<div class="abs section-title temp-title">Temperature control</div>
<svg class="abs" style="left:563px;top:221px" width="126" height="126" viewBox="0 0 126 126" aria-label="Thermostat">
  <defs>
    <linearGradient id="ringGrad" x1="0" x2="1"><stop offset="0" stop-color="#13aa4c"/><stop offset="0.5" stop-color="#a84a2a"/><stop offset="1" stop-color="#e5222a"/></linearGradient>
  </defs>
  <circle cx="63" cy="63" r="61" fill="none" stroke="url(#ringGrad)" stroke-width="3.5"/>
  <circle cx="63" cy="63" r="45" fill="url(#ringGrad)"/>
</svg>
<div class="abs temp-reading">23°C</div>
<div class="abs limit" style="top:230px">Max.</div>
<div class="abs limit" style="top:270px">Min.</div>

<div class="divider" style="left:893px"></div>

<div class="btn cool mode" style="top:170px">Normal</div>
<div class="btn cool mode" style="top:243px">Eco</div>
<div class="btn cool mode" style="top:322px">Off</div>

<!-- CCTV -->
<div class="abs section-title camera-title">CAMERA STREAMS</div>
<div class="abs camera-rule"></div>
<div class="stream" style="left:71px"><span class="num">01</span><svg width="16" height="18" viewBox="0 0 16 18"><path d="M0 0 L16 9 L0 18 Z" fill="#fff"/></svg></div>
<div class="stream" style="left:184px"><span class="num">02</span><svg width="16" height="18" viewBox="0 0 16 18"><path d="M0 0 L16 9 L0 18 Z" fill="#fff"/></svg></div>
<div class="stream" style="left:296px"><span class="num">03</span><svg width="16" height="18" viewBox="0 0 16 18"><path d="M0 0 L16 9 L0 18 Z" fill="#fff"/></svg></div>
<div class="stream" style="left:409px"><span class="num">04</span><svg width="16" height="18" viewBox="0 0 16 18"><path d="M0 0 L16 9 L0 18 Z" fill="#fff"/></svg></div>
<div class="stream" style="left:522px"><span class="num">05</span><svg width="16" height="18" viewBox="0 0 16 18"><path d="M0 0 L16 9 L0 18 Z" fill="#fff"/></svg></div>
<div class="stream" style="left:637px"><span class="num">05</span><svg width="16" height="18" viewBox="0 0 16 18"><path d="M0 0 L16 9 L0 18 Z" fill="#fff"/></svg></div>
<div class="stream" style="left:751px"><span class="num">05</span><svg width="16" height="18" viewBox="0 0 16 18"><path d="M0 0 L16 9 L0 18 Z" fill="#fff"/></svg></div>

<!-- Audio -->
<div class="btn cool audio audio-on" style="top:442px">AUDIO on</div>
<div class="btn cool audio" style="top:516px">Mute</div>

<svg class="abs speaker" style="top:446px" width="52" height="42" viewBox="0 0 52 42" aria-label="Audio on">
  <path d="M0 14 L10 14 L25 2 L25 40 L10 28 L0 28 Z" fill="#2f55b2"/>
  <g fill="none" stroke="#2f55b2" stroke-width="3" stroke-linecap="round">
    <path d="M31 14 A9 9 0 0 1 31 28"/><path d="M37 9 A15 15 0 0 1 37 33"/><path d="M43 4 A22 22 0 0 1 43 38"/>
  </g>
</svg>
<svg class="abs speaker" style="top:519px" width="62" height="46" viewBox="0 0 62 46" aria-label="Muted">
  <path d="M0 16 L10 16 L25 4 L25 42 L10 30 L0 30 Z" fill="#2f55b2"/>
  <g fill="none" stroke="#2f55b2" stroke-width="3" stroke-linecap="round">
    <path d="M31 16 A9 9 0 0 1 31 30"/><path d="M37 11 A15 15 0 0 1 37 35"/><path d="M43 6 A22 22 0 0 1 43 40"/>
  </g>
  <line x1="6" y1="44" x2="58" y2="2" stroke="#07144a" stroke-width="3"/>
</svg>

</body>
</html>
```